Book Cover for Productivity Book

I need a book cover for my latest publication "On Momentum: The Gathered Insights of the Busiest Woman Living"

You can see my branding at www.brightmarrow.example

This is meant to be my epic pinaccle work on productivity, I want it to look like the end all be all word on productivity.

Target Market(s)

entrepreneurs

```html
<!DOCTYPE html>
<html lang="en">
<head>
<meta charset="utf-8">
<title>On Momentum — Noa Brightwell</title>
<link href="https://fonts.googleapis.com/css2?family=Open+Sans:wght@300;400;700&display=swap" rel="stylesheet">
<style>
  :root {
    --paper: #ffffff;
    --ink: #3d3a3c;
    --accent: #d8464f;
    --crowd-light: #f1ecea;
    --crowd-pale: #fbf9f8;
  }
  html, body {
    margin: 0;
    padding: 0;
    overflow: hidden;
    background: var(--paper);
  }
  .cover {
    position: relative;
    width: 840px;
    height: 1200px;
    background: var(--paper);
    overflow: hidden;
    font-family: "Open Sans", sans-serif;
    color: var(--ink);
  }
  .cover__kicker {
    position: absolute;
    top: 98px;
    left: 0;
    width: 100%;
    text-align: center;
    font-weight: 300;
    font-size: 84px;
    line-height: 1;
    letter-spacing: 2px;
    margin: 0;
  }
  .cover__title {
    position: absolute;
    top: 190px;
    left: 0;
    width: 100%;
    text-align: center;
    font-weight: 700;
    font-size: 112px;
    line-height: 1;
    letter-spacing: 2px;
    color: var(--accent);
    margin: 0;
  }
  .cover__subtitle {
    position: absolute;
    top: 352px;
    left: 0;
    width: 100%;
    text-align: center;
    font-weight: 400;
    font-size: 30px;
    line-height: 38px;
    margin: 0;
  }
  .cover__art {
    position: absolute;
    left: 0;
    top: 420px;
    width: 840px;
    height: 780px;
  }
  .cover__author {
    position: absolute;
    right: 62px;
    bottom: 48px;
    font-size: 50px;
    line-height: 1;
    margin: 0;
    white-space: nowrap;
  }
  .cover__author-first {
    font-weight: 300;
  }
  .cover__author-last {
    font-weight: 700;
    color: var(--accent);
  }
</style>
</head>
<body>
  <main class="cover">
    <p class="cover__kicker">ON</p>
    <h1 class="cover__title">MOMENTUM</h1>
    <p class="cover__subtitle">The Gathered Insights of the<br>Busiest Woman Living</p>

    <svg class="cover__art" viewBox="0 420 840 780" role="img"
         aria-label="Illustration of a crowd of small standing people arranged into a large upward arrow pointing to the top right">
      <defs>
        <linearGradient id="arrowFill" x1="0" y1="1" x2="1" y2="0">
          <stop offset="0" stop-color="var(--crowd-pale)"/>
          <stop offset="1" stop-color="var(--crowd-light)"/>
        </linearGradient>
      </defs>
      <polygon points="40,1130 430,720 360,650 765,450 690,800 600,730 190,1190"
               fill="url(#arrowFill)"/>
    </svg>

    <p class="cover__author">
      <span class="cover__author-first">NOA</span>
      <span class="cover__author-last">BRIGHTWELL</span>
    </p>
  </main>
</body>
</html>
```